New Business Cards for MB&LR

We need updated business cards for a staff of 15 engineers, estimators, project managers, and sales people. We have recently begun changes to our website and marketing material to improve our look and branding. We are an established fabricator specializing in pressure vessels, tanks, and structural steel. The owners require us to use the existing logo and old english text design. Also, we prefer dark grey or mostly black cards.
Target Market(s)
Engineers, purchasing agents, estimators, and project managers of; mining companies, refineries, industrial construction professionals
Industry/Entity Type
Business
Contact Information for Business Card
Logo, phone, website, email, etc.
Look and feel

```html
<!DOCTYPE html>
<html lang="en">
<head>
<meta charset="utf-8">
<title>MB&amp;LR Business Cards</title>
<link href="https://fonts.googleapis.com/css2?family=Open+Sans:wght@400;700&display=swap" rel="stylesheet">
<style>
  :root {
    --backdrop: #2b2b2b;
    --paper: #f4f4f2;
    --ink: #151515;
    --band: #0d0d0d;
    --muted: #8a8a8a;
    --light-text: #f2f2f2;
  }
  * { margin: 0; padding: 0; box-sizing: border-box; }
  html, body {
    width: 1200px; height: 900px; overflow: hidden;
    background: var(--backdrop);
    font-family: "Open Sans", sans-serif;
  }
  .stage {
    position: relative; width: 1200px; height: 900px;
  }
  .card {
    position: absolute; left: 250px; width: 700px; height: 400px;
    overflow: hidden;
  }
  .card--front { top: 35px; background: var(--paper); }
  .card--back { top: 465px; background: var(--paper); }

  /* Front */
  .front-brand {
    position: absolute; inset: 0;
    display: flex; flex-direction: column; align-items: center; justify-content: center;
  }
  .brand-mark {
    display: flex; align-items: center; gap: 14px;
    margin-bottom: 26px;
  }
  .brand-mark__square {
    width: 34px; height: 34px; background: var(--ink);
  }
  .brand-mark__name {
    font-size: 44px; font-weight: 700; color: var(--ink); letter-spacing: 2px;
  }
  .company-name {
    font-size: 24px; font-weight: 700; color: var(--ink); letter-spacing: 0.5px;
  }
  .front-url {
    margin-top: 16px; font-size: 15px; color: var(--muted); letter-spacing: 7px;
  }

  /* Back */
  .back-band {
    position: absolute; left: 0; right: 0; top: 62px; bottom: 62px;
    background: var(--band);
  }
  .contact {
    position: absolute; left: 70px; top: 96px; width: 300px;
    color: var(--light-text);
  }
  .contact__name { font-size: 20px; font-weight: 700; letter-spacing: 1px; }
  .contact__role { font-size: 15px; margin-top: 2px; }
  .contact__rule { width: 40px; height: 1px; background: var(--light-text); margin: 14px 0; opacity: 0.7; }
  .contact__line { font-size: 14px; line-height: 1.55; }
  .back-brand {
    position: absolute; right: 70px; top: 62px; bottom: 62px;
    display: flex; align-items: center; gap: 14px;
  }
  .back-brand__square { width: 38px; height: 38px; background: var(--light-text); }
  .back-brand__name {
    font-size: 52px; font-weight: 700; color: var(--light-text); letter-spacing: 2px;
  }
</style>
</head>
<body>
<main class="stage">
  <section class="card card--front" aria-label="Card front">
    <div class="front-brand">
      <div class="brand-mark">
        <span class="brand-mark__square"></span>
        <span class="brand-mark__name">MB&amp;LR</span>
      </div>
      <p class="company-name">Mesa Beam &amp; Ledge Rolling</p>
      <p class="front-url">www.mbandlr.com</p>
    </div>
  </section>

  <section class="card card--back" aria-label="Card back">
    <div class="back-band"></div>
    <div class="contact">
      <p class="contact__name">ALEX CARTER</p>
      <p class="contact__role">CEO/FOUNDER</p>
      <div class="contact__rule"></div>
      <p class="contact__line">480 East 200 South</p>
      <p class="contact__line">Riverton Falls 84990</p>
      <div class="contact__rule"></div>
      <p class="contact__line">P : 555.210.4471</p>
      <p class="contact__line">F : 555.210.4472</p>
      <p class="contact__line">www.mbandlr.com</p>
    </div>
    <div class="back-brand">
      <span class="back-brand__square"></span>
      <span class="back-brand__name">MB&amp;LR</span>
    </div>
  </section>
</main>
</body>
</html>
```